Stationary and business card for an electrical contractor
Norvik Electric LLC
Stationary and business card for an electrical contractor - Construction
Creative Brief
Simple
Glen Hadley
President
412 N Orchard Ave
glen@norvikelectric-example.biz
WA Cont. # NORVIEL352TQ

```html
<!DOCTYPE html>
<html lang="en">
<head>
<meta charset="utf-8">
<title>Norvik Electric LLC — Business Card</title>
<link href="https://fonts.googleapis.com/css2?family=Roboto:ital,wght@0,400;0,700;0,900;1,400&display=swap" rel="stylesheet">
<style>
  :root {
    --page-bg: #e4e4e4;
    --brand-red: #e5203c;
    --brand-black: #111111;
    --card-white: #ffffff;
    --text-dark: #1c1c1c;
    --text-grey: #555555;
    --divider: #c9c9c9;
  }
  * { box-sizing: border-box; margin: 0; padding: 0; }
  html, body {
    width: 1200px; height: 901px; overflow: hidden;
    background: var(--page-bg);
    font-family: "Roboto", Arial, sans-serif;
  }
  .stage { position: relative; width: 1200px; height: 901px; }

  .card {
    position: absolute;
    width: 630px; height: 360px;
    border-radius: 16px;
    overflow: hidden;
    box-shadow: 0 10px 28px rgba(0,0,0,0.22);
  }

  /* Back side */
  .card-back { left: 500px; top: 48px; display: flex; }
  .card-back .red-field {
    width: 60%; background: var(--brand-red);
    position: relative;
  }
  .card-back .black-field {
    width: 40%; background: var(--brand-black);
    display: flex; align-items: center; justify-content: center;
  }
  .card-back .wordmark {
    position: absolute; left: 40px; top: 62px;
    color: var(--card-white);
    font-weight: 900; font-size: 40px; line-height: 1;
    text-transform: uppercase; letter-spacing: 1px;
  }
  .card-back .wordmark span { display: block; font-size: 30px; letter-spacing: 2px; margin-top: 4px; }
  .card-back .web {
    color: var(--card-white); font-style: italic; font-size: 14px;
    white-space: nowrap; margin-top: 70px;
  }

  /* Front side */
  .card-front {
    left: 90px; top: 470px;
    background: var(--card-white);
    border-top: 7px solid var(--brand-black);
    border-bottom: 12px solid var(--brand-red);
    display: flex; align-items: center;
  }
  .card-front .logo-block {
    width: 52%; display: flex; align-items: center; justify-content: center;
  }
  .card-front .wordmark {
    color: var(--brand-black);
    font-weight: 900; font-size: 40px; line-height: 1;
    text-transform: uppercase; letter-spacing: 1px; text-align: left;
  }
  .card-front .wordmark span { display: block; font-size: 30px; letter-spacing: 2px; margin-top: 4px; }
  .card-front .divider { width: 1px; height: 200px; background: var(--divider); }
  .card-front .contact { padding-left: 26px; color: var(--text-grey); font-size: 13px; line-height: 1.75; }
  .card-front .person-name { color: var(--brand-red); font-size: 20px; font-weight: 400; line-height: 1.2; }
  .card-front .person-title { color: var(--text-dark); font-size: 15px; margin-bottom: 6px; }
  .card-front .row { display: flex; align-items: center; gap: 8px; }
  .card-front .row svg { width: 12px; height: 12px; fill: var(--brand-red); flex: none; }
  .card-front .indent { padding-left: 20px; }
</style>
</head>
<body>
<main class="stage">

  <section class="card card-back" aria-label="Business card back">
    <div class="red-field">
      <div class="wordmark">Norvik<span>Electric</span></div>
    </div>
    <div class="black-field">
      <p class="web">www.norvikelectric-example.biz</p>
    </div>
  </section>

  <section class="card card-front" aria-label="Business card front">
    <div class="logo-block">
      <div class="wordmark">Norvik<span>Electric</span></div>
    </div>
    <div class="divider"></div>
    <div class="contact">
      <p class="person-name">Glen Hadley</p>
      <p class="person-title">President</p>
      <p class="indent">412 N Orchard Ave</p>
      <p class="indent">WA Cont. # NORVIEL352TQ</p>
      <p class="row">
        <svg viewBox="0 0 24 24" aria-hidden="true"><path d="M6.6 10.8a15.1 15.1 0 0 0 6.6 6.6l2.2-2.2a1 1 0 0 1 1-.25 11.4 11.4 0 0 0 3.6.57 1 1 0 0 1 1 1V20a1 1 0 0 1-1 1A17 17 0 0 1 3 4a1 1 0 0 1 1-1h3.5a1 1 0 0 1 1 1c0 1.25.2 2.45.57 3.57a1 1 0 0 1-.25 1z"/></svg>
        3605550148
      </p>
      <p class="row">
        <svg viewBox="0 0 24 24" aria-hidden="true"><path d="M2 5h20v14H2z M4 7v.5l8 5 8-5V7l-8 5z" fill-rule="evenodd"/></svg>
        glen@norvikelectric-example.biz
      </p>
      <p class="row">
        <svg viewBox="0 0 24 24" aria-hidden="true"><circle cx="12" cy="12" r="10"/></svg>
        www.norvikelectric-example.biz
      </p>
    </div>
  </section>

</main>
</body>
</html>
```